Book Cover and Back Cover for Assemble Yourself™ Career Development Manual
Daniel R. Holbrook | Holbrook Advisory, LLC | danielrholbrook.example
Book Cover and Back Cover for Assemble Yourself™ Career Development Manual - Books
Creative Brief
BOOK COVER - blue (RGB 0.0.69) is background/foundational color - the title, "Assemble Yourself™", is orange (RGB 255.54.0), is centered - the subtitle, "A blueprint for utilizing the TRAV assessment to unlock your potential, develop your career, and advance your personal brand." is white, is centered - my name, "Daniel R. Holbrook", is at the bottom, is centered - graphic...I'd like to add a graphic at the bottom of the cover, please review my website, danielrholbrook.example, for ideas. I want it to marry the ideas of business strategy concepts, unlocking human potential, and career growth. BACK COVER - blue (RGB 0.0.69) is background/foundational color - at top center, in orange (RGB 255.54.0), "Inside this manual is the process that will unlock your potential", in a thinly outlined box - in the center is the text "Daniel R. Holbrook is a Licensed Conduct Pattern Examiner (LCPE), a Principal Expert in Staff Affairs (PESA) and a Kestrel Institute of World Commerce MBA graduate. He is owner of Holbrook Advisory, LLC, a coaching practice specializing in unlocking human potential and career advancement, is author of a book entitled Dreading Ordinariness, and is Assistant Director of the L. T. Brandt College of Commerce' Graduate Career Center where he provides career coaching to professional programs MBA students. Daniel is also Vice Chairman of the Phoenix Enterprise and Labor Growth council. Prior to his current roles, he spent more than a decade in recruitment, training and development, and operations management with organizations such as the Bright Harbor Inns and Retreats, VacaLink Worldwide, Meridel Care, and Silver Mesa College." - my picture, from http://danielrholbrook.example/about-2/, is incorporated into the above biography text - standard empty white box for ISBN barcode, at the bottom right - the "Holbrook Advisory" business logo, at bottom left
Books
Working professionals who are: - trying to discover their life's purpose - wanting a promotion at their current job - trying to transition to a different employer - looking for a step-by-step process
JPEG and PDF in 300dpi commercial printing use for 8x11 book cover with bleed

```html
<!DOCTYPE html>
<html lang="en">
<head>
<meta charset="utf-8">
<title>Assemble Yourself™ — Book Cover Spread</title>
<link rel="stylesheet" href="https://fonts.googleapis.com/css2?family=Archivo+Narrow:wght@400;700&family=Arimo:wght@400;700&display=swap">
<style>
  :root {
    --navy: #000045;
    --spine: #00003a;
    --spine-edge: #0c0c5a;
    --orange: #ff3600;
    --white: #ffffff;
    --photo-tone: #6f7c8e;
  }
  * { margin: 0; padding: 0; box-sizing: border-box; }
  html, body { width: 1200px; height: 794px; overflow: hidden; background: var(--navy); }
  .spread {
    position: relative; width: 1200px; height: 794px;
    background: var(--navy);
    font-family: "Arimo", Arial, sans-serif;
    color: var(--white);
  }
  /* back cover */
  .back { position: absolute; left: 0; top: 0; width: 478px; height: 794px; }
  .back-headline {
    position: absolute; left: 43px; top: 34px; width: 401px; height: 100px;
    border: 1.5px solid var(--orange);
    padding: 0 8px;
    color: var(--orange);
    font-family: "Archivo Narrow", "Arial Narrow", sans-serif;
    font-weight: 700; font-size: 26px; line-height: 34px;
    display: flex; align-items: center; justify-content: center; text-align: center;
  }
  .bio {
    position: absolute; left: 86px; top: 180px; width: 370px;
    font-size: 12.2px; line-height: 22.6px; text-align: justify;
  }
  .author-photo {
    float: left; width: 78px; height: 94px; margin: 4px 12px 4px 0;
    background: linear-gradient(160deg, #8a97a8, var(--photo-tone) 60%, #3d4656);
  }
  .brand-mark {
    position: absolute; left: 44px; top: 680px; width: 130px;
    display: flex; flex-direction: column; align-items: center; gap: 6px;
    color: var(--white); font-size: 11px; font-weight: 700; letter-spacing: 0.5px; text-align: center;
  }
  .brand-mark .dot { width: 30px; height: 30px; border-radius: 50%; background: var(--white); }
  .isbn-box { position: absolute; left: 271px; top: 648px; width: 104px; height: 84px; background: var(--white); }
  /* spine */
  .spine {
    position: absolute; left: 478px; top: 0; width: 79px; height: 794px;
    background: var(--spine);
    border-left: 2px solid var(--spine-edge); border-right: 2px solid var(--spine-edge);
    overflow: hidden;
  }
  .spine-text {
    position: absolute; left: 50%; top: 22px;
    transform-origin: 0 0; transform: rotate(90deg) translateY(-50%);
    width: 750px; white-space: nowrap;
    display: flex; align-items: baseline; gap: 26px;
    font-family: "Archivo Narrow", "Arial Narrow", sans-serif;
    color: var(--orange);
  }
  .spine-author { font-size: 22px; }
  .spine-title { font-size: 52px; letter-spacing: 0.5px; }
  /* front cover */
  .front { position: absolute; left: 557px; top: 0; width: 643px; height: 794px; text-align: center; }
  .front-credit { position: absolute; top: 10px; width: 100%; color: var(--orange); font-size: 14.5px; }
  .front-title {
    position: absolute; top: 150px; width: 100%;
    color: var(--orange); font-weight: 400; font-size: 56px; line-height: 66px;
  }
  .front-subtitle {
    position: absolute; left: 80px; top: 336px; width: 490px;
    font-size: 19px; line-height: 27px;
  }
  .cover-art {
    position: absolute; left: 103px; top: 468px; width: 482px; height: 242px;
    background: linear-gradient(135deg, #cfd6de 0%, #8e9aa8 45%, #4a5564 100%);
  }
  .front-author { position: absolute; top: 738px; width: 100%; font-size: 34px; }
</style>
</head>
<body>
<main class="spread">
  <section class="back">
    <h2 class="back-headline">Inside this manual is the process that will unlock your potential</h2>
    <p class="bio"><span class="author-photo" role="img" aria-label="Portrait photograph of the author"></span>Daniel R. Holbrook is a Licensed Conduct Pattern Examiner (LCPE), a Principal Expert in Staff Affairs (PESA) and a Kestrel Institute of World Commerce MBA graduate. He is owner of Holbrook Advisory, LLC, a coaching practice specializing in unlocking human potential and career advancement, is author of a book entitled Dreading Ordinariness, and is Assistant Director of the L. T. Brandt College of Commerce' Graduate Career Center where he provides career coaching to professional programs MBA students. Daniel is also Vice Chairman of the Phoenix Enterprise and Labor Growth council. Prior to his current roles, he spent more than a decade in recruitment, training and development, and operations management with organizations such as the Bright Harbor Inns and Retreats, VacaLink Worldwide, Meridel Care, and Silver Mesa College.</p>
    <div class="brand-mark"><span class="dot"></span><span>HOLBROOK ADVISORY</span></div>
    <div class="isbn-box"></div>
  </section>

  <section class="spine">
    <div class="spine-text">
      <span class="spine-author">-Daniel R. Holbrook</span>
      <span class="spine-title">ASSEMBLE YOURSELF™</span>
    </div>
  </section>

  <section class="front">
    <p class="front-credit">Daniel R. Holbrook | Holbrook Advisory, LLC | danielrholbrook.example</p>
    <h1 class="front-title">ASSEMBLE<br>YOURSELF™</h1>
    <p class="front-subtitle">A blueprint for utilizing the TRAV assessment to unlock your potential, develop your career, and advance your personal brand.</p>
    <div class="cover-art" role="img" aria-label="Photo of a hand touching a sketched diagram of charts, gears and a light bulb representing strategy and growth"></div>
    <p class="front-author">-Daniel R. Holbrook</p>
  </section>
</main>
</body>
</html>
```